full company website for quellnorvi.com

full site with twitter, Facebook, leads capture, downloadable content, full services explanation pages, blogg, sexxy home page.

will pay additional funds other than pixel harbor payments..

fell free to contact me directly at maren . tolvik @ quellnorvi . com

```html
<!DOCTYPE html>
<html lang="en">
<head>
<meta charset="utf-8">
<title>Quellnorvi — Marketing, Sales &amp; Services Consulting</title>
<link rel="stylesheet" href="https://fonts.googleapis.com/css2?family=Oswald:wght@300;400;500&family=Josefin+Sans:wght@300;400&family=Arimo:wght@400;700&display=swap">
<style>
:root{
  --ink:#222222;
  --ink-soft:#555555;
  --text:#7a7a7a;
  --line:#d6d6d6;
  --band:#ececec;
  --white:#ffffff;
  --accent-blue:#3a8fd6;
  --photo-dark:#3c3c3c;
  --photo-light:#bdbdbd;
}
*{margin:0;padding:0;box-sizing:border-box}
html,body{width:835px;height:1200px;overflow:hidden;background:var(--white)}
body{font-family:"Arimo",Arial,sans-serif;color:var(--text)}
.page{position:relative;width:835px;height:1200px;overflow:hidden}
.abs{position:absolute}

.topbar{left:0;top:0;width:835px;height:19px;background:var(--ink);color:var(--white);font-size:8.5px;font-weight:700;text-align:center;line-height:19px}

.brand{display:flex;align-items:center;gap:8px;font-family:"Josefin Sans",sans-serif;font-weight:400;color:var(--ink-soft);white-space:nowrap}
.brand-mark{background:var(--ink-soft);flex:none}
.header-brand{left:134px;top:32px;font-size:34px;line-height:48px}
.header-brand .brand-mark{width:48px;height:48px}

.nav{top:38px;height:39px;font-family:"Oswald",sans-serif;font-size:11px;font-weight:300;color:var(--ink);line-height:39px;text-align:center;text-transform:uppercase;white-space:nowrap}
.nav.is-boxed{background:var(--ink);color:var(--white)}

.hero{left:0;top:96px;width:835px;height:310px;background:linear-gradient(110deg,var(--photo-dark) 0%,#8a8a8a 35%,#e4e4e4 55%,#9a9a9a 75%,var(--photo-light) 100%)}
.hero-arrow{width:24px;height:24px;top:238px}
.hero-caption{left:0;top:371px;width:835px;height:35px;background:rgba(40,40,40,.55);color:var(--white);font-family:"Josefin Sans",sans-serif;font-weight:300;font-size:15px;line-height:37px;text-align:center;white-space:nowrap}

.intro{left:0;top:406px;width:835px;height:96px;background:var(--band)}
.intro-title{left:133px;top:416px;font-family:"Oswald",sans-serif;font-weight:500;font-size:13px;color:var(--ink-soft)}
.intro-text{left:134px;top:440px;width:568px;font-size:9.5px;line-height:12px;text-align:center}
.intro-points{left:134px;top:472px;width:568px;display:flex;justify-content:center;gap:40px;font-size:9.5px;font-weight:700;color:var(--ink-soft);list-style:none}

.about{left:136px;top:517px;width:570px;font-size:9.5px;line-height:12px}
.about p+p{margin-top:12px}

.rule{height:1px;background:var(--line)}

.section-title{font-family:"Oswald",sans-serif;font-weight:400;font-size:12px;color:var(--ink-soft);text-transform:uppercase;white-space:nowrap}
.all-services{left:248px;top:609px;width:192px;height:24px;border:1px solid var(--line);font-family:"Oswald",sans-serif;font-weight:300;font-size:9.5px;color:var(--ink-soft);text-align:center;line-height:22px;text-transform:uppercase;white-space:nowrap}

.card{width:276px;height:143px;background:var(--white);border:1px solid #e4e4e4;border-radius:5px;box-shadow:2px 3px 4px rgba(0,0,0,.25)}
.card-title{position:absolute;left:9px;top:8px;font-family:"Oswald",sans-serif;font-weight:400;font-size:13px;line-height:16px;color:var(--ink-soft);text-transform:uppercase;white-space:nowrap}
.card-image{position:absolute;left:9px;top:28px;width:102px;height:90px;border:1px solid var(--line)}
.card-text{position:absolute;left:121px;top:28px;width:147px;font-size:9.5px;line-height:11px}
.card-more{position:absolute;right:7px;bottom:8px;width:57px;height:24px;background:var(--ink);color:var(--white);font-family:"Oswald",sans-serif;font-size:11px;text-align:center;line-height:24px}

.partners-title{left:0;top:986px;width:835px;text-align:center;font-family:"Oswald",sans-serif;font-weight:500;font-size:12.5px;color:var(--ink-soft)}
.partner{top:1014px;width:109px;height:38px;border:1px solid var(--line);display:flex;align-items:center;justify-content:center}
.partner span{display:block;width:70px;height:14px;background:#cfd3d8;border-radius:2px}

.footer{left:0;top:1078px;width:835px;height:100px;background:#f4f4f4;border-top:3px solid #cfcfcf}
.footer-heading{font-family:"Josefin Sans",sans-serif;font-weight:300;font-size:15px;color:var(--ink-soft);text-transform:uppercase}
.footer-links{font-size:8px;line-height:11px;color:var(--ink-soft);list-style:none}
.footer-brand{left:324px;top:1096px;font-size:25px;line-height:36px}
.footer-brand .brand-mark{width:36px;height:36px}
.footer-address{left:324px;top:1147px;width:170px;text-align:center;font-size:8px;line-height:10px;color:var(--ink-soft)}
.social{top:1157px;width:14px;height:14px;background:var(--accent-blue)}

.bottombar{left:0;top:1178px;width:835px;height:22px;background:var(--ink);color:var(--white);font-size:9px;font-weight:700;text-align:center;line-height:22px}
</style>
</head>
<body>
<div class="page">

  <div class="abs topbar">Marketing, Sales &amp; Services Enterprise Class Consulting - Pragmatic Strategies, Relentless Execution, Insightfull Measurements</div>

  <div class="abs brand header-brand"><span class="brand-mark"></span>Quellnorvi</div>

  <div class="abs nav is-boxed" style="left:427px;width:53px">Home</div>
  <div class="abs nav" style="left:486px;width:48px">Services</div>
  <div class="abs nav" style="left:538px;width:52px">Portfolio</div>
  <div class="abs nav" style="left:594px;width:50px">About Us</div>
  <div class="abs nav is-boxed" style="left:648px;width:54px">Contact</div>

  <div class="abs hero" role="img" aria-label="Black and white photograph of two business people shaking hands"></div>
  <svg class="abs hero-arrow" style="left:102px" viewBox="0 0 24 24" aria-hidden="true"><circle cx="12" cy="12" r="11" fill="rgba(60,60,60,.7)" stroke="#999"/><path d="M14 7l-5 5 5 5" fill="none" stroke="#ddd" stroke-width="2"/></svg>
  <svg class="abs hero-arrow" style="left:708px" viewBox="0 0 24 24" aria-hidden="true"><circle cx="12" cy="12" r="11" fill="rgba(120,120,120,.7)" stroke="#ccc"/><path d="M10 7l5 5-5 5" fill="none" stroke="#eee" stroke-width="2"/></svg>
  <div class="abs hero-caption">MARKETING, SALES &amp; SERVICES ENTERPRISE CLASS CONSULTING</div>

  <div class="abs intro"></div>
  <div class="abs intro-title">QUELLNORVI, INC.</div>
  <p class="abs intro-text">is a boutique consultancy focused on growing your business through Marketing , Sales and Service . We provide an expert services model by accompanying your existing organization to:</p>
  <ul class="abs intro-points">
    <li>• Develop strategies</li><li>• Build processes</li><li>• Implement technologies</li><li>• Deliver execution</li>
  </ul>

  <div class="abs about">
    <p>All this is as a natural extension of your group. We desire to stay in place through project delivery and business operation to ensure results and complete knowledge transfer from our team to yours.</p>
    <p>We pride ourselves on client success and growth; which is why we insist on the ability to teach , mentor , and cultivate your team as they work with our experts. Our goal is to ensure that when we leave, your success continues for years to come.</p>
  </div>

  <div class="abs rule" style="left:134px;top:594px;width:570px"></div>

  <h2 class="abs section-title" style="left:133px;top:612px">Some of our services</h2>
  <div class="abs all-services">Click here to see all our services</div>

  <article class="abs card" style="left:134px;top:649px">
    <h3 class="card-title">Service Management</h3>
    <div class="card-image" role="img" aria-label="Illustration of figures standing on a red target" style="background:linear-gradient(180deg,#f2f2f2,#d9d9d9 60%,#e05050)"></div>
    <p class="card-text">Service Management is designed to give your representatives a centralized repository of customer data and tools allowing them to deliver the best customer experience possible.</p>
    <div class="card-more">MORE</div>
  </article>

  <article class="abs card" style="left:427px;top:649px">
    <h3 class="card-title">Sales Management</h3>
    <div class="card-image" role="img" aria-label="Illustration of a silver sales funnel" style="background:radial-gradient(circle at 55% 50%,#9a9a9a,#f4f4f4 70%)"></div>
    <p class="card-text">Sales Management is the process of proactively optimizing the sales pipeline. Much like service management, this is done by providing your team with a complete customer picture of the sales opportunity;</p>
    <div class="card-more">MORE</div>
  </article>

  <article class="abs card" style="left:134px;top:811px">
    <h3 class="card-title">Reporting and Analytics</h3>
    <div class="card-image" role="img" aria-label="Illustration of a colourful bar chart on paper" style="background:linear-gradient(90deg,#f2f2f2,#9fd36a 40%,#f0b040 70%,#e84040)"></div>
    <p class="card-text">Reporting and analytics is about collecting, cleaning, and presenting both data and insights for business action.</p>
    <div class="card-more">MORE</div>
  </article>

  <article class="abs card" style="left:427px;top:811px">
    <h3 class="card-title">Enterprise Strategy</h3>
    <div class="card-image" role="img" aria-label="Diagram of a layered strategy pyramid" style="background:linear-gradient(180deg,#fbe4cc,#f2a060 60%,#9aa8c8)"></div>
    <p class="card-text">Enterprise Strategy is all about driving exponential growth by launching new products, expanding to new markets, changing pricing point, making emotional connections with the consumer ,and more.</p>
    <div class="card-more">MORE</div>
  </article>

  <div class="abs rule" style="left:0;top:974px;width:835px"></div>
  <h2 class="abs partners-title">And Look forward to enabling your success.</h2>
  <div class="abs partner" style="left:133px"><span></span></div>
  <div class="abs partner" style="left:248px"><span></span></div>
  <div class="abs partner" style="left:364px"><span></span></div>
  <div class="abs partner" style="left:479px"><span></span></div>
  <div class="abs partner" style="left:594px"><span></span></div>
  <div class="abs rule" style="left:0;top:1065px;width:835px"></div>

  <footer class="abs footer"></footer>
  <h3 class="abs footer-heading" style="left:134px;top:1090px">Sitemap</h3>
  <div class="abs rule" style="left:134px;top:1108px;width:162px"></div>
  <ul class="abs footer-links" style="left:134px;top:1116px"><li>Home</li><li>Services</li><li>Portfolio</li></ul>
  <ul class="abs footer-links" style="left:210px;top:1116px"><li>About Us</li><li>Contact</li></ul>

  <div class="abs brand footer-brand"><span class="brand-mark"></span>Quellnorvi</div>
  <p class="abs footer-address">Quellnorvi, Inc.<br>Complete Adress Here</p>

  <h3 class="abs footer-heading" style="left:524px;top:1090px">Contact</h3>
  <div class="abs rule" style="left:524px;top:1108px;width:162px"></div>
  <p class="abs footer-links" style="left:524px;top:1116px">Tel: 123.456.7890<br>Cell: 123.456.7890<br>Email: contact@quellnorvi.com</p>
  <div class="abs rule" style="left:524px;top:1150px;width:162px"></div>
  <span class="abs social" style="left:524px"></span>
  <span class="abs social" style="left:546px"></span>
  <span class="abs social" style="left:568px"></span>

  <div class="abs bottombar">Copyright © 2010 - 2014 Quellnorvi, Inc. All Rights Reserved.</div>
</div>
</body>
</html>
```